Toy Company Needs a Web Site For a New Toy

We need a web site for a new toy called "Zippa Loop Trike". The bike is a plastic, non motorized ride on toy for kids ages 1.5 - 5 years of age. The bike is being launched in three colors, red, blue and pink, though we may include a black option too.

For the web site we want something bold and colorful that communicates fun, therefore NO dull colors like black or grey. Nothing too cluttered. We want the site to attract the attention of kids but also give the parents a sense of confidence in our professionalism as a trustworthy toy company. The home page should focus on the bike, with different views of the bike and a small write-up on some of its key features. We would also like the home page to have a video of the bike in play. A obvious link to the shopping basket must be present as well. The site must include a shopping basket and ordering system.

Attached is a screenshot of a site that has the colourfulness and playfulness that we are looking for. Please have a look.

The bike images attached are renderings from the CAD software, actual high res photos will be used when the site is developed.

The product logo is attached and MUST be used on the site. It must be BOLD and can be incorporated into the actual website design.

The site pages are:
Home
Gallery
Buy
Contact

Competitors:
www.brambleplay.example
www.quorvaride.example
I do not like either of their sites.

We only have one product at this time, so the site is to be focused on that product, not a whole catalog of products. It is really a single product with the ability to purchase.
Updates

Project Deadline Extended
Reason: I am extending this competition in order to give me more time to review each design and provide the feedback that the designers deserve.

Target Market(s)

Parents, children ages 1.5 - 5.

Industry/Entity Type

It Company

Colors
0555a3
eb1f27
9bcb3c
faed22
f78f20
f37022
e34197
a6459a
6b449b

Requirements
Must have
• Please use the logo attached, but feel free to use different colors.
Should not have
• Dull colors like black and grey

```html
<!DOCTYPE html>
<html lang="en">
<head>
<meta charset="utf-8">
<title>Zippa Loop Trike</title>
<link href="https://fonts.googleapis.com/css2?family=Open+Sans:wght@400;600&family=Ultra&display=swap" rel="stylesheet">
<style>
  :root {
    --sky-blue: #35a4d9;
    --text-blue: #1f7db3;
    --deep-blue: #2280b3;
    --white: #ffffff;
    --player-dark: #2a2a2a;
    --player-mid: #4a4a4a;
    --progress-green: #5cc43c;
  }
  * { box-sizing: border-box; margin: 0; padding: 0; }
  html, body { width: 1200px; height: 771px; overflow: hidden; background: var(--white); }
  body { position: relative; font-family: "Open Sans", sans-serif; color: var(--text-blue); }

  .site-header { position: absolute; left: 0; top: 0; width: 1200px; height: 64px; background: var(--sky-blue); }
  .main-nav a {
    position: absolute; top: 21px; font-family: "Ultra", serif; font-size: 14px;
    color: var(--white); text-decoration: none; letter-spacing: 0.2px;
  }
  .nav-home { left: 250px; } .nav-about { left: 320px; } .nav-gallery { left: 392px; }
  .nav-buy { left: 777px; } .nav-contact { left: 837px; }
  .basket-link { position: absolute; left: 925px; top: 18px; width: 27px; height: 24px; }

  .brand-badge {
    position: absolute; left: 540px; top: 0; width: 124px; height: 122px;
    border-radius: 0 0 62px 62px; background: var(--sky-blue);
    display: flex; align-items: center; justify-content: center; z-index: 2;
  }
  .brand-badge .ring {
    width: 98px; height: 98px; border-radius: 50%; border: 3px solid var(--white);
    display: flex; align-items: center; justify-content: center; text-align: center;
    font-weight: 600; font-size: 12px; line-height: 1.2; color: var(--white);
    margin-top: 2px;
  }

  .landscape-banner {
    position: absolute; left: 0; top: 64px; width: 1200px; height: 142px;
    background: linear-gradient(180deg, #6fc0ea 0%, #b6def3 40%, #cfe7a8 62%, #a9d05a 80%, #8cc43f 100%);
  }

  .video-player {
    position: absolute; left: 249px; top: 269px; width: 368px; height: 257px;
    background: radial-gradient(ellipse at 50% 30%, var(--player-mid) 0%, var(--player-dark) 75%);
  }
  .video-player .play-big { position: absolute; left: 152px; top: 93px; }
  .control-bar {
    position: absolute; left: 1px; bottom: 1px; width: 366px; height: 24px;
    background: var(--sky-blue); display: flex; align-items: center;
    font-size: 6px; font-weight: 600; color: var(--white);
  }
  .control-bar .cb-play { width: 26px; height: 24px; border-right: 1px solid var(--deep-blue); display: flex; align-items: center; justify-content: center; }
  .control-bar .time { margin: 0 6px; }
  .control-bar .track { position: relative; width: 216px; height: 3px; background: #1d3f55; }
  .control-bar .track .buffered { position: absolute; left: 0; top: 0; width: 178px; height: 3px; background: #5f7788; }
  .control-bar .track .played { position: absolute; left: 0; top: 0; width: 124px; height: 3px; background: var(--progress-green); }
  .control-bar .track .knob { position: absolute; left: 120px; top: -2.5px; width: 8px; height: 8px; border-radius: 50%; background: #e8e8e8; }
  .control-bar .volume { display: flex; align-items: center; gap: 3px; }
  .control-bar .vol-bar { width: 22px; height: 2px; background: linear-gradient(90deg, var(--progress-green) 60%, #1d3f55 60%); }
  .control-bar .cb-full { margin-left: auto; width: 26px; height: 24px; border-left: 1px solid var(--deep-blue); display: flex; align-items: center; justify-content: center; }

  .video-caption { position: absolute; left: 249px; top: 535px; width: 380px; text-align: center; font-size: 12px; font-weight: 600; }

  .product-info { position: absolute; left: 654px; top: 263px; width: 296px; }
  .product-info h1 { font-size: 16px; font-weight: 600; text-align: center; margin-left: 0; width: 292px; margin-bottom: 7px; }
  .product-info p { font-size: 11.6px; line-height: 15px; margin-bottom: 15px; letter-spacing: 0.1px; }
  .buy-button {
    position: absolute; left: 96px; top: 248px; width: 94px; height: 26px;
    background: var(--sky-blue); color: var(--white); font-size: 12px;
    display: flex; align-items: center; justify-content: center; text-decoration: none; border-radius: 2px;
  }

  .site-footer { position: absolute; left: 0; top: 621px; width: 1200px; height: 150px; background: var(--sky-blue); color: var(--white); }
  .social-dot { position: absolute; left: 238px; top: 22px; width: 28px; height: 28px; border-radius: 50%; background: var(--white); }
  .tweet-card { position: absolute; left: 249px; top: 35px; width: 257px; height: 86px; background: var(--deep-blue); border-radius: 2px; font-size: 11.5px; }
  .tweet-card .handle { position: absolute; left: 18px; top: 19px; font-weight: 600; font-size: 12px; }
  .tweet-card .date { position: absolute; right: 20px; top: 19px; font-size: 11.5px; }
  .tweet-card .body { position: absolute; left: 20px; top: 36px; font-size: 11.5px; }
  .tweet-card .more { position: absolute; left: 20px; top: 54px; font-weight: 600; font-size: 11.5px; color: var(--white); text-decoration: none; }

  .footer-address { position: absolute; left: 619px; top: 33px; font-size: 11.5px; font-weight: 600; line-height: 14.5px; }
  .footer-address .label { margin-bottom: 8px; }
  .footer-tel { position: absolute; left: 862px; top: 35px; font-size: 11.5px; font-weight: 600; line-height: 14.5px; }
  .footer-tel .label { margin-bottom: 7px; }
  .copyright { position: absolute; left: 792px; top: 99px; font-size: 9.5px; }
</style>
</head>
<body>
  <header class="site-header">
    <nav class="main-nav">
      <a class="nav-home" href="#">Home</a>
      <a class="nav-about" href="#">About</a>
      <a class="nav-gallery" href="#">Gallery</a>
      <a class="nav-buy" href="#">Buy</a>
      <a class="nav-contact" href="#">Contact</a>
    </nav>
    <a class="basket-link" href="#" aria-label="Shopping basket">
      <svg width="27" height="24" viewBox="0 0 27 24">
        <path d="M8 8 L11 2 M19 8 L16 2" stroke="#fff" stroke-width="2.2" fill="none" stroke-linecap="round"/>
        <rect x="0" y="7" width="27" height="4" rx="1" fill="#fff"/>
        <path d="M2 12 H25 L23 24 H4 Z" fill="#fff"/>
        <rect x="6" y="14" width="15" height="2" fill="#35a4d9"/>
      </svg>
    </a>
  </header>

  <div class="brand-badge"><div class="ring">Zippa<br>Loop<br>Trike</div></div>

  <div class="landscape-banner" role="img" aria-label="Illustrated countryside of green fields and a winding river under a blue sky with clouds and a rainbow hot-air balloon"></div>

  <main>
    <div class="video-player">
      <svg class="play-big" width="52" height="52" viewBox="0 0 52 52" aria-label="Play video">
        <circle cx="26" cy="26" r="24" fill="#1c1c1c" stroke="#bdbdbd" stroke-width="3"/>
        <path d="M20 14 L38 26 L20 38 Z" fill="#fff"/>
      </svg>
      <div class="control-bar">
        <span class="cb-play"><svg width="9" height="10" viewBox="0 0 9 10"><path d="M0 0 L9 5 L0 10 Z" fill="#fff"/></svg></span>
        <span class="time">00:26</span>
        <span class="track"><span class="buffered"></span><span class="played"></span><span class="knob"></span></span>
        <span class="time">00:35</span>
        <span class="volume"><svg width="8" height="8" viewBox="0 0 8 8"><path d="M0 2.5 H2 L5 0 V8 L2 5.5 H0 Z" fill="#fff"/></svg><span class="vol-bar"></span></span>
        <span class="cb-full"><svg width="11" height="11" viewBox="0 0 11 11" fill="none" stroke="#fff" stroke-width="1.3"><path d="M0.5 3.5 V0.5 H3.5 M7.5 0.5 H10.5 V3.5 M10.5 7.5 V10.5 H7.5 M3.5 10.5 H0.5 V7.5"/></svg></span>
      </div>
    </div>
    <p class="video-caption">Please watch our short demonstration video</p>

    <section class="product-info">
      <h1>Product Information</h1>
      <p>Zippa Loop Trike is a new product which is safe, very durable and easy to clean.</p>
      <p>Dummy text is text that is used in the publishing industry or by web designers to occupy the space which will later be filled with ‘real’ content. This is required when, for example, the final text is not yet available.</p>
      <p>It is said that song composers of the past used dummy texts as lyrics when writing melodies in order to have a ‘ready-made’ text to sing with the melody. Dummy texts have been in use by typesetters since the 16th century.</p>
      <a class="buy-button" href="#">Buy Now</a>
    </section>
  </main>

  <footer class="site-footer">
    <div class="tweet-card">
      <span class="handle">@zippalooptrike</span>
      <span class="date">Oct 23rd</span>
      <span class="body">Today we sold our 10,000th Zippa Loop!!</span>
      <a class="more" href="#">read more......</a>
    </div>
    <span class="social-dot"></span>
    <address class="footer-address" style="font-style:normal">
      <div class="label">Address:</div>
      Zippa Loop Trike<br>7 Pedal Row<br>Eastbrook Vale<br>EB4 2QL
    </address>
    <div class="footer-tel">
      <div class="label">Tel:</div>
      01632 960412
    </div>
    <p class="copyright">Copyright © 2013 Zippa Loop Trike</p>
  </footer>
</body>
</html>
```